PawNook business card

Looking for a fun and cool biz card for a new company with patent pending products. I have products to help and protect dogs hearing. My colors are pantone blue and orange.
Updates

Please add tag line: Protect the ones you love...even your PawNooks!

Target Market(s)

Animal/Dog lovers!

Industry/Entity Type

Retail

Contact Information for Business Card

I'm looking for something simple yet fun with all the info included for biz cards

Colors
0555a3
f78f20

Requirements
Must have
• Logo
Nice to have
• name, website and email
Should not have
• phone number

```html
<!DOCTYPE html>
<html lang="en">
<head>
<meta charset="utf-8">
<title>PawNook Business Card</title>
<link rel="stylesheet" href="https://fonts.googleapis.com/css2?family=Work+Sans:wght@400;500;700&display=swap">
<style>
  :root {
    --page-bg: #d9d4cf;
    --card-clear: #eceae7;
    --card-edge: #f7f6f4;
    --brand-orange: #dc4b26;
    --brand-orange-deep: #c8401f;
    --brand-blue: #0555a3;
    --text-light: #f1e7e2;
    --text-soft: #f3d2c6;
  }
  * { box-sizing: border-box; margin: 0; padding: 0; }
  html, body {
    width: 1200px;
    height: 1047px;
    overflow: hidden;
    background: var(--page-bg);
    font-family: "Work Sans", Arial, sans-serif;
  }
  .business-card {
    position: absolute;
    left: 100px;
    top: 252px;
    width: 1000px;
    height: 543px;
    border-radius: 26px;
    background: var(--card-clear);
    border: 2px solid var(--card-edge);
    overflow: hidden;
    box-shadow: 0 18px 40px rgba(60, 45, 35, 0.18);
  }
  .orange-panel {
    position: absolute;
    inset: 0;
    background: linear-gradient(135deg, var(--brand-orange) 0%, var(--brand-orange-deep) 100%);
    clip-path: polygon(0 0, 69% 0, 64% 100%, 0 100%);
  }
  .brand-mark {
    position: absolute;
    left: 590px;
    top: 62px;
    width: 410px;
    height: 410px;
    border-radius: 50%;
    background: var(--brand-blue);
  }
  .card-content {
    position: absolute;
    left: 63px;
    top: 78px;
    color: var(--text-light);
  }
  .brand-name {
    font-weight: 700;
    font-size: 84px;
    line-height: 1;
    letter-spacing: -1px;
    color: var(--text-light);
  }
  .tagline {
    margin-top: 14px;
    font-size: 20px;
    font-weight: 500;
    color: var(--text-light);
  }
  .person-name {
    margin-top: 52px;
    font-weight: 500;
    font-size: 31px;
    letter-spacing: 0.5px;
    text-transform: uppercase;
  }
  .person-role {
    margin-top: 4px;
    font-size: 22px;
    color: var(--text-soft);
  }
  .address {
    margin-top: 28px;
    font-size: 23px;
    line-height: 30px;
    letter-spacing: 0.4px;
    color: var(--text-soft);
    font-style: normal;
  }
  .contact-list {
    list-style: none;
    margin-top: 26px;
    font-size: 23px;
    letter-spacing: 0.4px;
    color: var(--text-soft);
  }
  .contact-item {
    display: flex;
    align-items: center;
    height: 31px;
  }
  .contact-icon {
    width: 15px;
    height: 15px;
    margin-right: 22px;
    flex: none;
  }
</style>
</head>
<body>
  <section class="business-card">
    <div class="orange-panel"></div>
    <div class="brand-mark" aria-hidden="true"></div>
    <div class="card-content">
      <div class="brand-name">PawNook</div>
      <p class="tagline">Protect the ones you love...even your PawNooks!</p>
      <div class="person-name">Daniel Reyes</div>
      <div class="person-role">Director</div>
      <address class="address">318 Linden Ave. Suite<br>Oregon OR 97201</address>
      <ul class="contact-list">
        <li class="contact-item">
          <svg class="contact-icon" viewBox="0 0 16 16" aria-hidden="true"><rect x="1.5" y="3.5" width="13" height="9" rx="1" fill="none" stroke="currentColor" stroke-width="1.6"/><path d="M2 4.5l6 4.5 6-4.5" fill="none" stroke="currentColor" stroke-width="1.6"/></svg>
          <span>info@pawnook.com</span>
        </li>
        <li class="contact-item">
          <svg class="contact-icon" viewBox="0 0 16 16" aria-hidden="true"><circle cx="8" cy="8" r="6.5" fill="none" stroke="currentColor" stroke-width="1.5"/><ellipse cx="8" cy="8" rx="2.8" ry="6.5" fill="none" stroke="currentColor" stroke-width="1.3"/><path d="M1.5 8h13" stroke="currentColor" stroke-width="1.3"/></svg>
          <span>www.pawnook.com</span>
        </li>
      </ul>
    </div>
  </section>
</body>
</html>
```